2 banners brivon brand stories / tools / gastronomy

We need 2 banners each for the brand stories on Brivon.
The banners should have the following formats:
(1464px x 625px and 463px x 625px).
2x banner for the brand plomin
2x banners for the brand KALDUR
The banner should be relatively neutral with the logo. Like the example I uploaded.

Brivon

```html
<!DOCTYPE html>
<html lang="en">
<head>
<meta charset="utf-8">
<title>Brivon brand story banners</title>
<link rel="stylesheet" href="https://fonts.googleapis.com/css2?family=Michroma&family=Quicksand:wght@600&display=swap">
<style>
  :root {
    --page: #ffffff;
    --ink: #ffffff;
    --night: #050505;
    --coal: #131313;
    --smoke: #2e2e2e;
  }
  html, body {
    margin: 0;
    padding: 0;
    width: 1200px;
    height: 905px;
    overflow: hidden;
    background: var(--page);
  }
  .sheet {
    position: relative;
    width: 1200px;
    height: 905px;
  }
  .banner {
    position: absolute;
    overflow: hidden;
    background: var(--night);
  }
  .banner--wide { left: 57px; width: 773px; height: 349px; }
  .banner--tall { left: 894px; width: 233px; height: 334px; }
  .row-one { top: 72px; }
  .row-two { top: 482px; }

  .texture {
    position: absolute;
    inset: 0;
    background:
      radial-gradient(ellipse 38% 55% at 8% 85%, var(--smoke) 0%, rgba(46,46,46,0) 100%),
      radial-gradient(ellipse 30% 50% at 95% 22%, var(--smoke) 0%, rgba(46,46,46,0) 100%),
      linear-gradient(100deg, var(--coal) 0%, var(--night) 55%, #0a0a0a 100%);
  }
  .banner--tall .texture {
    background:
      radial-gradient(ellipse 70% 45% at 15% 85%, var(--smoke) 0%, rgba(46,46,46,0) 100%),
      linear-gradient(160deg, var(--coal) 0%, var(--night) 60%, #0b0b0b 100%);
  }

  .brand {
    position: absolute;
    display: flex;
    align-items: center;
    color: var(--ink);
  }
  .brand__dot { display: block; flex: none; }
  .brand__name {
    font-family: "Michroma", sans-serif;
    font-weight: 400;
    line-height: 1;
    white-space: nowrap;
  }
  .brand--wide { left: 22px; top: 24px; gap: 6px; }
  .brand--wide .brand__name { font-size: 26px; letter-spacing: 3px; }
  .brand--small { left: 16px; top: 21px; gap: 4px; }
  .brand--small .brand__name { font-size: 12.5px; letter-spacing: 1.5px; }

  .brand--round { left: 16px; top: 15px; }
  .brand--round .brand__name {
    font-family: "Quicksand", sans-serif;
    font-weight: 600;
    font-size: 28px;
    letter-spacing: 0.5px;
  }
</style>
</head>
<body>
<main class="sheet">

  <section class="banner banner--wide row-one">
    <div class="texture" role="img" aria-label="Dark backdrop with faint grey rounded diamond pattern and a large subtle brand mark"></div>
    <div class="brand brand--wide">
      <svg class="brand__dot" width="34" height="34" viewBox="0 0 34 34" aria-hidden="true">
        <circle cx="17" cy="17" r="15" fill="none" stroke="#ffffff" stroke-width="3"/>
      </svg>
      <span class="brand__name">KALDUR</span>
    </div>
  </section>

  <section class="banner banner--tall row-one">
    <div class="texture" role="img" aria-label="Dark backdrop with faint grey rounded diamond pattern and a large subtle brand mark"></div>
    <div class="brand brand--small">
      <svg class="brand__dot" width="16" height="16" viewBox="0 0 16 16" aria-hidden="true">
        <circle cx="8" cy="8" r="6.8" fill="none" stroke="#ffffff" stroke-width="1.5"/>
      </svg>
      <span class="brand__name">KALDUR</span>
    </div>
  </section>

  <section class="banner banner--wide row-two">
    <div class="texture" role="img" aria-label="Dark backdrop with faint grey rounded diamond pattern and a large subtle brand mark"></div>
    <div class="brand brand--wide">
      <svg class="brand__dot" width="34" height="34" viewBox="0 0 34 34" aria-hidden="true">
        <circle cx="17" cy="17" r="15" fill="none" stroke="#ffffff" stroke-width="3"/>
      </svg>
      <span class="brand__name">KALDUR</span>
    </div>
  </section>

  <section class="banner banner--tall row-two">
    <div class="texture" role="img" aria-label="Dark backdrop with faint grey rounded diamond pattern and a large subtle diagonal brand mark"></div>
    <div class="brand brand--round">
      <span class="brand__name">plomin</span>
    </div>
  </section>

</main>
</body>
</html>
```